Velmora Group LLC (need a packaging design for vodka Sarvok)

We need a packaging design for a new product. Our product will be vodka. The name of the product is Sarvok. Sarvok means the name of the mountain also Sarvok has another meaning which is God of nomad people from Central Asia. Sarvok will be bottled in 750 ml bottle. We will be using organically grown and clean ingredients for making vodka. The main ingredients is clean Artezian water. Designs should show mountains, symbol of virginity of nature. Designs must be bright, unique and attractive.

```html
<!DOCTYPE html>
<html lang="en">
<head>
<meta charset="utf-8">
<title>Sarvok Vodka Label</title>
<link rel="stylesheet" href="https://fonts.googleapis.com/css2?family=Roboto:wght@900&family=Pinyon+Script&family=Open+Sans:wght@400&display=swap">
<style>
  :root {
    --page: #ffffff;
    --label-navy: #0a3b6f;
    --mist-light: #5a9fd8;
    --mist-mid: #2f6fae;
    --snow: #ffffff;
    --accent-blue: #64a6dc;
    --wolf-blue: #1b88cb;
    --edge: #1a1a1a;
  }
  * { margin: 0; padding: 0; box-sizing: border-box; }
  html, body {
    width: 914px;
    height: 1200px;
    overflow: hidden;
    background: var(--page);
  }
  .canvas {
    position: relative;
    width: 914px;
    height: 1200px;
  }
  .label {
    position: absolute;
    left: 125px;
    top: 158px;
    width: 664px;
    height: 893px;
    background: var(--label-navy);
    border: 1px solid var(--edge);
    overflow: hidden;
  }
  .sky-texture {
    position: absolute;
    left: 0;
    top: 0;
    width: 664px;
    height: 290px;
    background:
      radial-gradient(ellipse 180px 60px at 150px 50px, rgba(90,159,216,0.85), transparent 75%),
      radial-gradient(ellipse 360px 120px at 420px 90px, rgba(47,111,174,0.7), transparent 75%),
      radial-gradient(ellipse 220px 110px at 580px 200px, rgba(47,111,174,0.55), transparent 75%);
  }
  .mountain-range {
    position: absolute;
    left: 140px;
    top: 117px;
    width: 368px;
    height: 110px;
  }
  .wolf-emblem {
    position: absolute;
    left: 15px;
    top: 612px;
    width: 160px;
    height: 275px;
  }
  .brand-name {
    position: absolute;
    left: 0;
    width: 100%;
    top: 236px;
    text-align: center;
    font-family: "Roboto", Arial, sans-serif;
    font-weight: 900;
    font-size: 138px;
    line-height: 1;
    color: var(--snow);
    letter-spacing: -1px;
    padding-right: 20px;
  }
  .script-line {
    position: absolute;
    left: 0;
    width: 100%;
    text-align: center;
    font-family: "Pinyon Script", cursive;
    line-height: 1;
    padding-right: 20px;
  }
  .tagline-premium { top: 395px; font-size: 44px; color: var(--snow); }
  .product-type { top: 448px; font-size: 86px; color: var(--accent-blue); }
  .tagline-nature { top: 548px; font-size: 40px; color: var(--snow); }
  .volume-info {
    position: absolute;
    left: 0;
    width: 100%;
    top: 824px;
    text-align: center;
    font-family: "Open Sans", Arial, sans-serif;
    font-size: 20px;
    color: var(--snow);
    padding-right: 8px;
  }
</style>
</head>
<body>
<main class="canvas">
  <section class="label">
    <div class="sky-texture" role="img" aria-label="Speckled misty sky texture in light blue"></div>
    <svg class="mountain-range" role="img" aria-label="Illustration of snow-capped mountain peaks" viewBox="0 0 368 110">
      <rect width="368" height="110" rx="6" fill="#c9dcee"/>
    </svg>
    <h1 class="brand-name">Sarvok</h1>
    <p class="script-line tagline-premium">Premium Quality</p>
    <p class="script-line product-type">Vodka</p>
    <p class="script-line tagline-nature">The Virginity of Nature</p>
    <svg class="wolf-emblem" role="img" aria-label="Line illustration of a howling wolf" viewBox="0 0 160 275">
      <rect width="160" height="275" rx="6" fill="var(--wolf-blue)" opacity="0.55"/>
    </svg>
    <p class="volume-info">40% vol.&nbsp; –&nbsp; 75 cl.</p>
  </section>
</main>
</body>
</html>
```